Travel video blogger needs website design

I need a website designed for my new travel video blog "Roaming Sparrow". I have only just started but need a website that is fairly simple and not too busy. I have a logo which I want on it (I have attached it to this project). I also want a link to all my other social medias on the main page (vidtrekhub, Snapwell and Palnook) and my videos as well. Here is a link to my vidtrekhub page for you to look at: https://www.vidtrekhub.net/channel/QRm4tZ8pWnE2HX57YKccd31v
As I have only just started and I am still trying to find my specific niche, again I need it to be sleek and simple that I can go in and change slightly here and there. I would like these pages on the website: About Me, Videos, Social Media, Blog, Gallery, contact me. for an example I like the look of www.theroamingkinfolk.net website.

I already have the domain and I am with Harborweb with pagecraftr.org. I just want to spend my time getting better and learning about videos then trying to create a website (I am a bit of a perfectionist when I try to do something).

Target Market(s)

Young Adults (majority females) between the ages of 18 and 30 with an interest in travelling.

Industry/Entity Type

Travel Industry

Number of Pages Required

1 page

Colors

Designer to choose colors to be used in the design.

Requirements
Must have
• A like to my Snapwell, Palnook and vidtrekhub channels on the home page
• Must be a nice, simple design
• Must have my logo on the front and name "Roaming Sparrow"
Nice to have
• A nice light, bright coloured theme
Should not have
• A dark coloured theme

```html
<!DOCTYPE html>
<html lang="en">
<head>
<meta charset="utf-8">
<title>Roaming Sparrow – Travel Video Blog</title>
<link rel="stylesheet" href="https://fonts.googleapis.com/css2?family=Arimo:wght@400;600&family=Lora:wght@400&display=swap">
<style>
  :root {
    --gold: #d8b27e;
    --ink: #1c1c1c;
    --nav-ink: #222222;
    --white: #ffffff;
    --paper: #fbfaf8;
    --sea: #a9c3cf;
    --foam: #dfe8eb;
    --sand: #b8ada2;
    --warm: #c9a88e;
  }
  * { box-sizing: border-box; margin: 0; padding: 0; }
  html, body { width: 1200px; height: 625px; overflow: hidden; }
  body {
    position: relative;
    background: var(--paper);
    font-family: "Arimo", Arial, sans-serif;
    color: var(--ink);
  }

  /* Top navigation */
  .topbar {
    position: absolute; left: 0; top: 0; width: 1200px; height: 30px;
    background: var(--paper);
  }
  .social-links {
    position: absolute; left: 234px; top: 11px;
    display: flex; gap: 8px; list-style: none;
  }
  .social-links a {
    font-size: 9px; font-weight: 600; color: var(--gold);
    text-decoration: none; line-height: 10px;
  }
  .main-nav {
    position: absolute; top: 0; left: 394px;
    display: flex; list-style: none;
  }
  .main-nav li { margin-right: 22px; }
  .main-nav a {
    display: block; padding-top: 11px; height: 30px;
    font-size: 10.2px; color: var(--nav-ink); text-decoration: none;
    text-transform: uppercase;
  }
  .main-nav .current a { color: var(--gold); border-top: 2px solid var(--gold); padding-top: 9px; }
  .search-button {
    position: absolute; left: 947px; top: 7px; width: 18px; height: 18px;
    border-radius: 50%; background: var(--gold);
  }
  .search-button svg { position: absolute; left: 4px; top: 4px; }

  /* Brand */
  .brand {
    position: absolute; left: 0; top: 30px; width: 1200px; height: 120px;
    background: var(--white);
    display: flex; flex-direction: column; align-items: center;
  }
  .brand-mark {
    margin-top: 14px; width: 52px; height: 52px;
    border: 2px solid var(--ink); border-radius: 50%;
  }
  .brand-name {
    margin-top: 22px; font-size: 14px; font-weight: 600;
    letter-spacing: 1px; text-transform: uppercase; color: var(--ink);
  }

  /* Hero */
  .hero {
    position: absolute; left: 0; top: 150px; width: 1200px; height: 336px;
    background:
      linear-gradient(90deg, transparent 0%, transparent 55%, rgba(201,168,142,0.55) 80%, rgba(160,110,95,0.5) 100%),
      linear-gradient(180deg, var(--sea) 0%, var(--foam) 50%, var(--sand) 78%, #a99f95 100%);
  }
  .feature-card {
    position: absolute; left: 431px; top: 245px; width: 329px; height: 146px;
    background: var(--white); text-align: center;
  }
  .feature-frame {
    position: absolute; left: 441px; top: 254px; width: 328px; height: 146px;
    border: 2px solid var(--gold);
  }
  .feature-category {
    margin-top: 25px; font-size: 10.5px; color: var(--gold);
    text-transform: uppercase; letter-spacing: 0.3px;
  }
  .feature-title {
    margin-top: 6px; font-family: "Lora", Georgia, serif; font-weight: 400;
    font-size: 22px; line-height: 28px; color: var(--ink);
  }
  .feature-link {
    display: inline-block; margin-top: 10px;
    font-family: "Lora", Georgia, serif; font-size: 11.5px;
    color: var(--ink); text-decoration: underline;
  }

  /* Section tiles */
  .tiles {
    position: absolute; left: 234px; top: 458px;
    display: flex; gap: 24px; list-style: none;
  }
  .tile {
    position: relative; width: 225px; height: 144px; overflow: hidden;
  }
  .tile-blog { background: linear-gradient(135deg, #a66b52 0%, #c9a77c 50%, #4e6b6d 100%); }
  .tile-about { background: linear-gradient(160deg, #d9cbb4 0%, #6f7f84 45%, #c8b9a2 100%); }
  .tile-videos { background: linear-gradient(180deg, #e7b46a 0%, #b5703a 50%, #3a2b24 100%); }
  .tile-label {
    position: absolute; left: 0; right: 0; bottom: 10px; text-align: center;
    font-family: "Lora", Georgia, serif; font-size: 18px; color: var(--white);
  }
  .play-icon { position: absolute; left: 101px; top: 60px; }
</style>
</head>
<body>
  <header class="topbar">
    <ul class="social-links">
      <li><a href="#">Snapwell</a></li>
      <li><a href="#">Palnook</a></li>
      <li><a href="https://www.vidtrekhub.net/channel/QRm4tZ8pWnE2HX57YKccd31v">Vidtrekhub</a></li>
    </ul>
    <ul class="main-nav">
      <li class="current"><a href="#">About Me</a></li>
      <li><a href="#">Videos</a></li>
      <li><a href="#">Social Media</a></li>
      <li><a href="#">Blog</a></li>
      <li><a href="#">Gallery</a></li>
      <li><a href="#">Contact Me</a></li>
    </ul>
    <span class="search-button" aria-label="Search">
      <svg width="10" height="10" viewBox="0 0 10 10"><circle cx="4" cy="4" r="2.8" fill="none" stroke="#fff" stroke-width="1.4"/><line x1="6.1" y1="6.1" x2="9" y2="9" stroke="#fff" stroke-width="1.6" stroke-linecap="round"/></svg>
    </span>
  </header>

  <div class="brand">
    <span class="brand-mark"></span>
    <span class="brand-name">Roaming Sparrow</span>
  </div>

  <section class="hero" role="img" aria-label="Photo of a woman holding a wide-brim hat on a beach with waves"></section>
  <div class="feature-frame"></div>
  <article class="feature-card">
    <p class="feature-category">Good Feelings</p>
    <h1 class="feature-title">Good Feelings Come From<br>Good Heart</h1>
    <a class="feature-link" href="#">Read More</a>
  </article>

  <ul class="tiles">
    <li class="tile tile-blog" role="img" aria-label="Photo of a straw hat, camera and juice on a table">
      <span class="tile-label">The Blog</span>
    </li>
    <li class="tile tile-about" role="img" aria-label="Photo of a woman in a sun hat on coastal rocks">
      <span class="tile-label">About Me</span>
    </li>
    <li class="tile tile-videos" role="img" aria-label="Photo of friends celebrating on a hill at sunset">
      <svg class="play-icon" width="22" height="26" viewBox="0 0 22 26"><polygon points="0,0 22,13 0,26" fill="#ffffff" fill-opacity="0.75"/></svg>
      <span class="tile-label">Videos</span>
    </li>
  </ul>
</body>
</html>
```